Initial website for sport tech startup

We are currently in the R&D phases of our new product. It’s a headband to prevent concussion in the soccer market initially.

We have 2 products, one that’s basic aimed at the youth market and the other more technology driven that’s aimed at the academies and professional market.

Initially the product will launch in the UK

Target Market(s)

Youth soccer players and parents in UK, Soccer Clubs, Federations.

Industry/Entity Type

Sporting Good

Coding

Coded - Design and coding required

Number of Pages Required

5+ page

Requirements
Must have
• Professional style that can be adapted and changed over the coming months.
Nice to have
• Ecommerce ability in the future.

```html
<!DOCTYPE html>
<html lang="en">
<head>
<meta charset="utf-8">
<title>KOVRA – V1 Headband</title>
<link href="https://fonts.googleapis.com/css2?family=Jost:wght@400;500;600;700&display=swap" rel="stylesheet">
<style>
:root{
  --ink:#231f20;
  --nav-active:#58585a;
  --brand-blue:#005b94;
  --accent-blue:#3a9bd0;
  --button-blue:#1e88d8;
  --paper:#f4f4f4;
  --paper-edge:#dcdcdc;
  --rule:#cfcfcf;
  --muted:#7a7a7a;
  --card:#e1e1e1;
  --water:#5b8590;
  --globe:#3d3f42;
  --check:#a95a4a;
  --white:#fff;
}
*{box-sizing:border-box;margin:0;padding:0}
html,body{width:1067px;height:1200px;overflow:hidden}
body{font-family:'Jost',sans-serif;color:#111;position:relative;
  background:radial-gradient(ellipse at 50% 45%,var(--white) 0%,var(--paper) 40%,var(--paper-edge) 100%)}
.abs{position:absolute}

.site-header{position:absolute;left:0;top:0;width:1067px;height:80px;background:var(--ink)}
.brand{position:absolute;left:20px;top:11px;width:249px;height:58px;border:4px solid var(--brand-blue);
  display:flex;align-items:center;justify-content:center;color:var(--white);font-weight:500;font-size:38px;letter-spacing:2px}
.main-nav{position:absolute;right:0;top:0;height:80px;display:flex}
.main-nav a{display:block;height:80px;line-height:78px;padding:0 8px;color:var(--white);text-decoration:none;font-size:24px;letter-spacing:.5px}
.main-nav a.active{background:var(--nav-active)}
.main-nav a:last-child{padding-right:48px}

.title-rule{position:absolute;height:6px;background:var(--brand-blue);top:164px}
.page-title{position:absolute;left:100px;top:122px;width:540px;font-size:81px;font-weight:700;color:var(--brand-blue);line-height:1;white-space:nowrap}

.gallery-frame{left:159px;top:248px;width:336px;height:336px;border:2px solid var(--ink);border-radius:4px}
.gallery-image{left:207px;top:349px;width:240px;height:143px;background:var(--white)}
.gallery-image div{position:absolute;left:20px;top:12px;width:205px;height:122px;border-radius:40px 30px 60px 20px;
  background:linear-gradient(160deg,#66707c,#4b5561)}
.arrow{top:358px;width:62px;height:88px;background:var(--ink);border-radius:4px;display:flex;align-items:center;justify-content:center}
.thumb{top:607px;width:73px;height:73px;border:1px solid #c9c9c9;background:#f7f7f7}
.thumb div{position:absolute;left:10px;top:22px;width:52px;height:30px;background:linear-gradient(160deg,#fff,#e9e9e9);}
.thumb div::after{content:"";position:absolute;left:4px;top:3px;width:44px;height:22px;border-radius:10px 6px 14px 4px;background:#7d838a}

.section-heading{font-weight:600;font-size:26px;line-height:1;color:#111;white-space:nowrap}
.quick-copy{left:583px;top:300px;width:418px;font-size:19px;line-height:19.5px;color:#111}
.price{left:592px;top:421px;width:115px;height:73px;border:2px solid var(--ink);border-radius:9px;
  display:flex;align-items:center;justify-content:center;font-size:46px;font-weight:700}
.feature{top:428px;width:46px;height:37px;display:flex;align-items:center;justify-content:center}
.qty-label{left:583px;top:520px;font-size:19px}
.qty-step{top:523px;width:21px;height:21px;border:1px solid var(--ink);background:#eee;font-size:18px;font-weight:700;
  display:flex;align-items:center;justify-content:center;line-height:1}
.qty-input{left:709px;top:517px;width:63px;height:34px;border:1px solid #999;background:#f3f3f3;font-size:24px;font-weight:500;
  display:flex;align-items:center;justify-content:center}
.add-cart{left:811px;top:517px;width:161px;height:34px;background:#000;color:var(--white);font-size:26px;white-space:nowrap;
  display:flex;align-items:center;justify-content:center}

.divider{left:0;top:699px;width:1067px;height:2px;background:var(--rule)}

.testimonial{left:93px;top:796px;width:412px;height:237px;background:var(--card)}
.avatar{left:8px;top:7px;width:69px;height:69px;border-radius:50%;background:radial-gradient(circle,#c9a99a,#b23a3a)}
.person-name{left:104px;top:12px;font-size:19px;font-weight:700;color:var(--accent-blue);letter-spacing:.5px;white-space:nowrap}
.person-role{left:104px;top:36px;font-size:17.5px;color:var(--muted);white-space:nowrap}
.quote{left:104px;top:68px;width:300px;font-size:18.5px;line-height:24px;color:var(--muted)}

.product-card{left:741px;top:791px;width:174px;height:240px;background:var(--white);border:1px solid #bbb;border-radius:10px;
  box-shadow:2px 4px 6px rgba(0,0,0,.35);text-align:center}
.product-card h3{font-weight:500;font-size:19px;line-height:1;margin-top:9px}
.product-card .sub{font-size:13px;line-height:1}
.product-art{position:absolute;left:43px;top:44px;width:90px;height:52px;border-radius:16px 10px 22px 6px;background:linear-gradient(160deg,#f27a8a,#e2475c)}
.product-card p{position:absolute;left:11px;top:104px;width:154px;text-align:left;font-size:6.8px;line-height:9.2px}
.mini-icons{position:absolute;left:40px;top:176px;display:flex;gap:10px}
.coming{position:absolute;left:28px;top:207px;width:117px;height:25px;background:var(--button-blue);border-radius:3px;color:var(--white);
  font-size:12.5px;line-height:1;white-space:nowrap;display:flex;align-items:center;justify-content:center}

.partner{top:1075px;height:44px;background:#9a9a9a;opacity:.7}

.site-footer{position:absolute;left:0;top:1134px;width:1067px;height:66px;background:var(--ink);color:var(--white);font-size:13.5px}
.tagline{position:absolute;left:274px;top:22px;display:flex;align-items:center;gap:8px;white-space:nowrap}
.tagline .bar{width:2px;height:21px;background:var(--button-blue)}
.contact{position:absolute;left:671px;display:flex;align-items:center;gap:4px;white-space:nowrap}
</style>
</head>
<body>
<header class="site-header">
  <div class="brand">KOVRA</div>
  <nav class="main-nav">
    <a href="#">PRODUCTS</a>
    <a href="#" class="active">ABOUT US</a>
    <a href="#">LOGIN</a>
  </nav>
</header>

<div class="title-rule" style="left:0;width:92px"></div>
<h1 class="page-title">V1 Headband</h1>
<div class="title-rule" style="left:645px;width:422px"></div>

<div class="abs gallery-frame"></div>
<div class="abs gallery-image" role="img" aria-label="Grey V1 headband product photo"><div></div></div>
<div class="abs arrow" style="left:127px"><svg width="32" height="40" viewBox="0 0 32 40"><path d="M26 6 8 20l18 14" fill="none" stroke="#fff" stroke-width="8" stroke-linejoin="round"/></svg></div>
<div class="abs arrow" style="left:464px"><svg width="32" height="40" viewBox="0 0 32 40"><path d="M6 6l18 14L6 34" fill="none" stroke="#fff" stroke-width="8" stroke-linejoin="round"/></svg></div>
<div class="abs thumb" style="left:105px" role="img" aria-label="Headband view 1"><div></div></div>
<div class="abs thumb" style="left:197px" role="img" aria-label="Headband view 2"><div></div></div>
<div class="abs thumb" style="left:290px" role="img" aria-label="Headband view 3"><div></div></div>
<div class="abs thumb" style="left:383px" role="img" aria-label="Headband view 4"><div></div></div>
<div class="abs thumb" style="left:476px" role="img" aria-label="Headband view 5"><div></div></div>

<h2 class="abs section-heading" style="left:581px;top:256px">Quick Description</h2>
<p class="abs quick-copy">Lorem ipsum dolor sit amet, consectetur adipiscing elit, sed do eiusmod tempor incididunt ut labore et dolore magna aliqua. Quis ipsum suspendisse ultrices gravida. Risus commodo viverra maecenas accumsan lacus vel facilisis.</p>
<div class="abs price">£49</div>
<div class="abs feature" style="left:805px;background:var(--water)"><svg width="20" height="22" viewBox="0 0 20 22"><path d="M10 2C6 8 4 11 4 14a6 6 0 0 0 12 0c0-3-2-6-6-12z" fill="#fff"/></svg></div>
<div class="abs feature" style="left:866px;background:var(--globe)"><svg width="22" height="22" viewBox="0 0 22 22" fill="none" stroke="#fff" stroke-width="1.6"><circle cx="11" cy="11" r="9"/><ellipse cx="11" cy="11" rx="4" ry="9"/><path d="M2 11h18M4 6h14M4 16h14"/></svg></div>
<div class="abs feature" style="left:928px;background:var(--check)"><svg width="24" height="24" viewBox="0 0 24 24" fill="none" stroke="#fff" stroke-width="1.6"><rect x="4" y="4" width="13" height="17" rx="1"/><path d="M8 3h5v3H8zM7 10h7M7 13h7M7 16h4"/><circle cx="18" cy="18" r="4" fill="#fff"/><path d="M16 18l1.5 1.5L20 17" stroke="var(--check)"/></svg></div>
<div class="abs qty-label">Quantity:</div>
<div class="abs qty-step" style="left:682px">-</div>
<div class="abs qty-input">3</div>
<div class="abs qty-step" style="left:778px">+</div>
<div class="abs add-cart">Add to Cart</div>

<div class="abs divider"></div>

<h2 class="abs section-heading" style="left:225px;top:745px">Testimonials</h2>
<h2 class="abs section-heading" style="left:669px;top:745px">Other Products from Us</h2>

<div class="abs testimonial">
  <div class="abs avatar" role="img" aria-label="Portrait of the chief executive"></div>
  <div class="abs person-name">MARTIN ELLERY</div>
  <div class="abs person-role">– Chief Executive Officer</div>
  <p class="abs quote">From leading edge technology to white label product distribution and most recently sport. Martin has excelled as a leader of start-ups and has worked with sporting clubs and federations across UK &amp; Europe.</p>
</div>

<div class="abs product-card">
  <h3>V2 Headband</h3>
  <div class="sub">with Tracker!</div>
  <div class="product-art" role="img" aria-label="Pink V2 headband product image"></div>
  <p>Now represents the opportunity to develop a head protection product for use in contact sports to help reduce the impact of concussion and product a fool proof way of measuring temperature in a post pandemic world, accepting that there is no such thing as concussion-proof head protection.</p>
  <div class="mini-icons">
    <svg width="16" height="16" viewBox="0 0 16 16" fill="none" stroke="#222"><path d="M8 1l6 2v5c0 3-3 6-6 7-3-1-6-4-6-7V3z"/><circle cx="8" cy="8" r="2.5"/></svg>
    <svg width="16" height="16" viewBox="0 0 16 16" fill="none" stroke="#222"><path d="M8 1C5 6 3 8 3 10a5 5 0 0 0 10 0c0-2-2-4-5-9z"/></svg>
    <svg width="16" height="16" viewBox="0 0 16 16" fill="none" stroke="#222"><path d="M2 15C4 9 8 3 15 1 14 8 9 12 3 13M2 15l7-8"/></svg>
    <svg width="16" height="16" viewBox="0 0 16 16" fill="none" stroke="#222"><circle cx="6" cy="10" r="3.5"/><circle cx="12" cy="4" r="2.5"/></svg>
  </div>
  <div class="coming">COMING SOON!</div>
</div>

<div class="abs partner" style="left:185px;width:113px;border-radius:4px"></div>
<div class="abs partner" style="left:351px;width:112px;border-radius:22px"></div>
<div class="abs partner" style="left:514px;width:32px;border-radius:50%"></div>
<div class="abs partner" style="left:594px;width:96px;border-radius:4px"></div>
<div class="abs partner" style="left:734px;width:34px;border-radius:4px 4px 17px 17px"></div>
<div class="abs partner" style="left:805px;width:85px;height:36px;border-radius:2px"></div>

<footer class="site-footer">
  <div class="tagline"><span>KOVRA LTD</span><span class="bar"></span><span>Making Sport Safer</span></div>
  <div class="contact" style="top:12px"><svg width="16" height="16" viewBox="0 0 16 16"><path d="M3 1l3 3-2 2c1 2 3 4 5 5l2-2 3 3-2 3C7 15 1 9 1 3z" fill="#fff"/></svg>+44 20 7946 0321</div>
  <div class="contact" style="top:36px"><svg width="16" height="12" viewBox="0 0 16 12"><rect x=".5" y=".5" width="15" height="11" fill="#fff"/><path d="M1 1l7 6 7-6M1 11l5-5M15 11l-5-5" fill="none" stroke="#231f20"/></svg>hello@kovra.co.uk</div>
</footer>
</body>
</html>
```